Advert for Services that we offer

Bolt Remova Ltd need an design to represent what we do in a modern way by showing an image with a brief description and the use of corporate logo the information we will proved vie a doc file and this is to be presented in a modern way. This design will be for print & web. we have done our own design and its not great i have put this in the file repository

Target Market(s)

Motor trade

Font styles to use
Sans Serif

Colors

Designer to choose colors to be used in the design.

Requirements
Must have
• Company colour scheme as per logo within the files uploaded.
• and a small boarder to isolate it from the rest of the articles.
Nice to have
• Modern font
Should not have
• Old style font

```html
<!DOCTYPE html>
<html lang="en">
<head>
<meta charset="utf-8">
<title>Product Testing &amp; Analysis – Bolt Remova Ltd</title>
<link href="https://fonts.googleapis.com/css2?family=Orbitron:wght@800;900&family=Fira+Sans:wght@400;500&family=Fira+Sans+Condensed:wght@500&display=swap" rel="stylesheet">
<style>
  :root {
    --page: #f4f4f4;
    --white: #ffffff;
    --blue: #1b6fc8;
    --blue-deep: #0f5cb0;
    --blue-light: #3f97e0;
    --grey: #a3a3a6;
    --grey-light: #d9d9db;
    --text-light: #ffffff;
  }
  * { margin: 0; padding: 0; box-sizing: border-box; }
  html, body { width: 1200px; height: 827px; overflow: hidden; background: var(--page); }
  .advert {
    position: absolute; left: 20px; top: 87px;
    width: 1160px; height: 652px;
    background: var(--white);
    border: 1px solid var(--grey-light);
    overflow: hidden;
    font-family: "Fira Sans", sans-serif;
  }
  .advert__shapes { position: absolute; inset: 0; }
  .headline {
    position: absolute; left: 24px; top: 20px; width: 1110px;
    font-family: "Orbitron", sans-serif; font-weight: 900;
    font-size: 47px; letter-spacing: 1px; line-height: 50px;
    color: var(--blue); text-align: center; white-space: nowrap;
  }
  .website {
    position: absolute; left: 245px; top: 94px;
    font-size: 25px; color: var(--text-light); line-height: 32px;
  }
  .services { position: absolute; left: 0; top: 160px; list-style: none; }
  .services__item {
    position: absolute; left: 131px; white-space: nowrap;
    font-family: "Fira Sans Condensed", sans-serif; font-weight: 500;
    font-size: 37px; line-height: 44px; color: var(--text-light);
  }
  .brand {
    position: absolute; left: 862px; top: 140px; width: 272px;
    display: flex; align-items: center; gap: 10px;
    font-family: "Fira Sans", sans-serif; font-weight: 500;
    font-size: 25px; color: var(--blue); white-space: nowrap;
  }
  .brand__mark { width: 26px; height: 26px; background: var(--blue); flex: none; }
  .phone {
    position: absolute; left: 108px; top: 581px;
    font-family: "Orbitron", sans-serif; font-weight: 800;
    font-size: 37px; line-height: 48px; color: var(--text-light); letter-spacing: 1px;
  }
  .follow {
    position: absolute; left: 630px; top: 564px;
    font-size: 29px; line-height: 32px; color: var(--blue);
  }
  .social { position: absolute; left: 631px; top: 612px; display: flex; gap: 10px; }
  .social__square { width: 28px; height: 28px; border-radius: 4px; background: var(--blue); }
</style>
</head>
<body>
<main class="advert">
  <svg class="advert__shapes" width="1160" height="652" viewBox="0 0 1160 652" aria-hidden="false">
    <defs>
      <linearGradient id="panelGradient" x1="0" y1="0" x2="1" y2="1">
        <stop offset="0" stop-color="#1d6ec6"/>
        <stop offset="0.55" stop-color="#3f97e0"/>
        <stop offset="1" stop-color="#1f73cb"/>
      </linearGradient>
      <linearGradient id="photoGradient" x1="0" y1="0" x2="1" y2="1">
        <stop offset="0" stop-color="#d8d6d2"/>
        <stop offset="0.5" stop-color="#9a948e"/>
        <stop offset="1" stop-color="#4a4a4e"/>
      </linearGradient>
      <linearGradient id="greyBand" x1="0" y1="0" x2="1" y2="0">
        <stop offset="0" stop-color="#e8e8ea"/>
        <stop offset="1" stop-color="#bdbdc0"/>
      </linearGradient>
      <linearGradient id="rowShade" x1="0" y1="0" x2="1" y2="0">
        <stop offset="0" stop-color="#0d4f9c" stop-opacity="0.45"/>
        <stop offset="1" stop-color="#0d4f9c" stop-opacity="0"/>
      </linearGradient>
    </defs>

    <!-- top grey strip and web bar -->
    <polygon points="0,91 170,91 146,128 0,128" fill="var(--grey)"/>
    <polygon points="184,91 848,91 822,140 160,140" fill="var(--blue-deep)"/>

    <!-- outer chevron edge -->
    <path d="M0,128 L822,128 L848,91 L760,300 Q728,375 764,440 L870,652 L0,652 Z" fill="var(--blue-deep)"/>
    <!-- main panel -->
    <path d="M0,128 L785,128 L700,320 Q672,380 708,440 L780,555 L0,555 Z" fill="url(#panelGradient)"/>

    <!-- service row shading -->
    <rect x="90" y="162" width="540" height="70" fill="url(#rowShade)"/>
    <rect x="90" y="309" width="540" height="70" fill="url(#rowShade)"/>
    <rect x="90" y="456" width="540" height="70" fill="url(#rowShade)"/>

    <!-- diamond icon holders -->
    <g fill="#dcdde0" stroke="#b7b9be" stroke-width="2">
      <rect x="62" y="175" width="44" height="44" rx="6" transform="rotate(45 84 197)"/>
      <rect x="62" y="249" width="44" height="44" rx="6" transform="rotate(45 84 271)"/>
      <rect x="62" y="322" width="44" height="44" rx="6" transform="rotate(45 84 344)"/>
      <rect x="62" y="396" width="44" height="44" rx="6" transform="rotate(45 84 418)"/>
      <rect x="62" y="470" width="44" height="44" rx="6" transform="rotate(45 84 492)"/>
    </g>
    <!-- simple icons -->
    <g fill="none" stroke="var(--blue)" stroke-width="3" stroke-linecap="round" stroke-linejoin="round">
      <path d="M72,207 L72,192 L84,184 L96,192 L96,207 Z"/>
      <circle cx="84" cy="271" r="12"/><circle cx="84" cy="271" r="5"/>
      <path d="M70,338 h22 v14 h-22 z M92,348 h6"/>
      <path d="M74,405 h16 v26 h-16 z M78,413 h8 M78,419 h8 M78,425 h5"/>
      <path d="M73,503 v-10 M80,503 v-16 M87,503 v-12 M94,503 v-20"/>
    </g>

    <!-- photograph area -->
    <path role="img" aria-label="Technician measuring the bore of a red bearing housing with a dial gauge in a workshop"
          d="M820,219 L1160,219 L1160,652 L875,652 L752,455 Q735,432 752,405 Z" fill="url(#photoGradient)"/>

    <!-- bottom grey band -->
    <path d="M0,555 L740,555 L790,652 L0,652 Z" fill="url(#greyBand)"/>
    <path d="M0,566 Q0,571 10,571 L560,571 Q575,571 585,580 L636,652 L0,652 Z" fill="var(--blue)"/>

    <!-- phone icon -->
    <path d="M45,596 q-8,6 -4,18 q8,18 24,26 q10,4 16,-4 l-8,-8 q-4,4 -8,2 q-8,-5 -12,-14 q-2,-4 2,-8 Z" fill="var(--white)"/>
    <path d="M64,596 q10,4 12,14 M66,588 q16,5 18,22" stroke="var(--white)" stroke-width="3" fill="none" stroke-linecap="round"/>

    <!-- globe icon -->
    <g fill="none" stroke="var(--white)" stroke-width="2">
      <circle cx="230" cy="110" r="11"/>
      <ellipse cx="230" cy="110" rx="5" ry="11"/>
      <path d="M219,110 h22 M221,104 h18 M221,116 h18"/>
    </g>

    <!-- brand rules -->
    <line x1="862" y1="184" x2="1134" y2="184" stroke="var(--blue)" stroke-width="1.5"/>
  </svg>

  <h1 class="headline">PRODUCT TESTING &amp; ANALYSIS</h1>
  <p class="website">www.bolt-remova.co.uk</p>

  <div class="brand">
    <span class="brand__mark"></span>
    <span class="brand__name">Bolt Remova Ltd</span>
  </div>

  <ul class="services">
    <li class="services__item" style="top:14px">Metallurgical testing</li>
    <li class="services__item" style="top:88px">Bearing pre-load testing</li>
    <li class="services__item" style="top:161px">Bore measurement</li>
    <li class="services__item" style="top:235px">New product evaluation</li>
    <li class="services__item" style="top:309px">Product analysis &amp; report</li>
  </ul>

  <p class="phone">(0161) 555 0192</p>

  <p class="follow">Follow us</p>
  <div class="social" aria-label="Social media links">
    <span class="social__square"></span>
    <span class="social__square"></span>
    <span class="social__square"></span>
    <span class="social__square"></span>
  </div>
</main>
</body>
</html>
```